High end personal training flyer design

I want a flyer designed to be delivered to people's houses to interest them in high end (and, therefore, not cheap) personal training services.

Don't want standard pictures of people exercising, before and afters, etc. More something that will appeal to that more affluent market.

Flexible on size of flyer, but please make sure it is a standard size that I can get printed easily. Would like it not to look like a normal flyer you get through the letterbox, so if any particular sizes, shapes, etc are known to do that, then that would be a good start.

Text on flyer to be as follows:

Is this you:

Live in East Cheshire
Male, aged 30-50
A father
Cash rich, time poor
Find handling high pressure at work comfortable
But have a short fuse out of work – with the wife, kids, life in general, etc
Not happy with the way your body looks and feels
Know exactly what you should do to sort that, but struggling to actually do it for various reasons
Turned off by the standard menu of options for addressing that – gyms, slimming clubs, diets, etc

If so, you may be interested in what I do.

Some would call it Personal Training. Some would call it Coaching. I’m not interested in giving what I do labels.

What I am interested in is providing the best possible service (and results) for my clients – whatever that entails.

I work closely with one or two clients at a time to make sure they get exactly what they need.

If you would like to find out more about this, I usually meet for a coffee and a chat. To see if we both think our working together is a good idea.

No squeeze pages, no countdowns, mailing lists or false scarcity.

No plastering this flyer with ‘Before and afters’ – they are ten a penny and my clients don’t want to have pictures of them in their underwear spread around the local area.

Just give me a call and we’ll go from there.

My number is 07914562208.

Ray

Industry/Entity Type

Training

Requirements
Should not have
• Generic before and after or exercise type pictures

```html
<!DOCTYPE html>
<html lang="en">
<head>
<meta charset="utf-8">
<title>Is This You? – Personal Training Flyer</title>
<link href="https://fonts.googleapis.com/css2?family=Bebas+Neue&family=Archivo+Black&family=Arimo:wght@400&display=swap" rel="stylesheet">
<style>
  :root {
    --page: #f0eed8;
    --panel-dark: #222222;
    --ink-light: #f4f4f4;
    --ink-dark: #141414;
    --photo-grey-1: #8f908e;
    --photo-grey-2: #c9c9c7;
    --photo-grey-3: #dcdbd8;
    --photo-warm: #e2c7ae;
  }
  * { margin: 0; padding: 0; box-sizing: border-box; }
  html, body {
    width: 1200px; height: 900px; overflow: hidden;
    background: var(--page);
  }
  .flyer {
    position: absolute; left: 22px; top: 22px;
    width: 1158px; height: 821px;
    font-family: "Arimo", Arial, sans-serif;
  }
  .flyer__left {
    position: absolute; left: 0; top: 0; width: 551px; height: 100%;
    background: var(--panel-dark); color: var(--ink-light);
  }
  .flyer__right {
    position: absolute; left: 551px; top: 0; width: 607px; height: 100%;
    color: var(--ink-dark); overflow: hidden;
  }
  .portrait {
    position: absolute; inset: 0;
    background:
      radial-gradient(ellipse 340px 520px at 560px 520px, var(--photo-warm) 0%, rgba(226,199,174,0.6) 45%, rgba(226,199,174,0) 75%),
      linear-gradient(90deg, var(--photo-grey-1) 0%, var(--photo-grey-2) 30%, var(--photo-grey-3) 65%, var(--photo-grey-2) 100%);
  }
  .heading-block {
    position: absolute;
    font-family: "Archivo Black", "Arial Black", sans-serif;
    font-size: 18px; letter-spacing: 0.3px; line-height: 1;
  }
  .body-copy {
    position: absolute;
    font-size: 14.6px; line-height: 18.3px; letter-spacing: 0.4px;
    text-transform: uppercase;
  }
  .body-copy p + p { margin-top: 18.3px; }
  .display {
    position: absolute;
    font-family: "Bebas Neue", Impact, sans-serif;
    line-height: 0.9;
  }

  .profile-title { left: 46px; top: 48px; }
  .profile-list { left: 46px; top: 78px; }
  .issues-title { right: 28px; top: 118px; text-align: right; }
  .issues-list { right: 28px; top: 150px; text-align: right; }
  .invite { left: 46px; top: 522px; width: 482px; }
  .call-label { left: 46px; top: 640px; font-size: 36px; }
  .call-number { left: 44px; top: 673px; font-size: 76px; letter-spacing: 0.5px; }

  .headline { right: 50px; top: 48px; font-size: 80px; }
  .ifso-title { left: 50px; top: 118px; }
  .ifso-copy { left: 50px; top: 150px; }
  .sign-intro { left: 50px; top: 640px; font-size: 36px; }
  .sign-name { left: 50px; top: 673px; font-size: 76px; }
</style>
</head>
<body>
<main class="flyer">
  <section class="flyer__left">
    <h2 class="heading-block profile-title">YOUR PROFILE?</h2>
    <div class="body-copy profile-list">
      Live in East Cheshire?<br>Male, aged 30-50?<br>A father?
    </div>

    <h2 class="heading-block issues-title">YOUR ISSUES?</h2>
    <div class="body-copy issues-list">
      <p>Cash rich, time poor?</p>
      <p>Find handling high pressure at work?</p>
      <p>Comfortable but have a short fuse out of work<br>with the wife, kids, life in general, etc?</p>
      <p>Not happy with the way your body looks and feels?</p>
      <p>Know exactly what you should do to sort that,<br>but struggling to actually do it<br>for various reasons?</p>
      <p>Turned off by the standard<br>menu of options for addressing that<br>gyms, slimming clubs, diets, etc?</p>
    </div>

    <p class="body-copy invite">If you would like to find out more about this, I usually meet for a coffee and a chat. To see if we both think our working together is a good idea.</p>

    <p class="display call-label">CALL ME ON</p>
    <p class="display call-number">07914562208</p>
  </section>

  <section class="flyer__right">
    <div class="portrait" role="img" aria-label="Close-up portrait photograph of the trainer, cropped to half his face with glasses, against a grey studio backdrop"></div>

    <h1 class="display headline">IS THIS YOU?</h1>

    <h2 class="heading-block ifso-title">IF SO?</h2>
    <div class="body-copy ifso-copy">
      <p>You may be interested<br>in what I do</p>
      <p>Some would call it<br>personal training.<br>Some would call it<br>coaching. I’m not interested<br>in giving what I do labels.</p>
      <p>What I am interested in<br>is providing the best<br>possible service<br>(and results)<br>for my clients<br>whatever that entails.</p>
      <p>I work closely with<br>one or two clients<br>at a time to make sure<br>they get exactly<br>what they need.</p>
    </div>

    <p class="display sign-intro">I’M</p>
    <p class="display sign-name">RAY MARSH</p>
  </section>
</main>
</body>
</html>
```